ARC VOLLEY Business Card Project

I'd like to request a business card design for the new company I've launched.
The name of the company is "ARC VOLLEY" an indoor unmanned tennis practice facility.
We would like to see designs that use our brand identity color in the logo I've attached.
We hope to get the design with modern, luxurious and elegant tone and manner.
We hope the logo should not be too big.

Business card must have elements as below:
- Logo (One of the logos I've attached)
- Name (In Korean Text) : 박 서 윤
- Title (In Korean Text) : 대표
- Phone Number : 010-8472-3916
- Email Address : seoyun.park@arcvolley-example.co.kr
- Website : www.arcvolley-example.co.kr
- Instagram : arcvolley
- Address (In Korean text) : 경기도 용인시 수지구 풍덕천로 456 미래타워 5층 501호, 502호

Target Market(s)

Tennis amateurs in 20 to 40s

Industry/Entity Type

Sports, Hobby

Contact Information for Business Card

- Logo (One of the logos I've attached) - Name (In Korean Text) : 박 서 윤 - Title (In Korean Text) : 대표 - Phone Number : 010-8472-3916 - Email Address : seoyun.park@arcvolley-example.co.kr - Website : www.arcvolley-example.co.kr - Instagram : arcvolley - Address (In Korean text) : 경기도 용인시 수지구 풍덕천로 456 미래타워 5층 501호, 502호

Font styles to use
Sans Serif

Requirements
Must have
• Double sided
Nice to have
• Logo with intaglio or relief embossing
Should not have
• Logo should not be too big.

```html
<!DOCTYPE html>
<html lang="ko">
<head>
<meta charset="UTF-8">
<title>ARC VOLLEY Business Card</title>
<link href="https://fonts.googleapis.com/css2?family=Noto+Sans+KR:wght@300;400;500;700&display=swap" rel="stylesheet">
<style>
  :root {
    --bg: #e4e4e6;
    --paper: #ffffff;
    --green: #2e5a3c;
    --green-deep: #1e4d2b;
    --ink-light: #ffffff;
    --ink-dark: #2a2a2a;
  }
  * { margin: 0; padding: 0; box-sizing: border-box; }
  html, body {
    width: 1200px; height: 800px; overflow: hidden;
    background: var(--bg);
    font-family: "Noto Sans KR", sans-serif;
  }
  .canvas { position: relative; width: 1200px; height: 800px; }
  .card {
    position: absolute; top: 250px;
    width: 540px; height: 300px; overflow: hidden;
    box-shadow: 0 6px 18px rgba(0,0,0,0.15);
  }
  .card-shape { position: absolute; inset: 0; width: 100%; height: 100%; }
  .card--front { left: 40px; background: var(--paper); }
  .card--back { left: 620px; background: var(--green); }

  .front-website {
    position: absolute; left: 30px; top: 30px;
    font-size: 13px; letter-spacing: 1.5px; color: var(--ink-dark);
    font-weight: 400; white-space: nowrap;
  }
  .brand {
    position: absolute; display: flex; align-items: center; gap: 8px;
    font-weight: 700; letter-spacing: 1.5px; white-space: nowrap;
  }
  .brand-dot { border-radius: 50%; flex: none; }
  .card--front .brand { left: 352px; top: 140px; color: var(--green-deep); font-size: 20px; }
  .card--front .brand-dot { width: 28px; height: 28px; background: var(--green-deep); }
  .card--back .brand { right: 24px; bottom: 20px; color: var(--ink-light); font-size: 19px; }
  .card--back .brand-dot { width: 24px; height: 24px; background: var(--ink-light); }

  .contact { position: absolute; left: 34px; top: 24px; color: var(--ink-light); }
  .contact-name { font-size: 18px; font-weight: 500; letter-spacing: 4px; line-height: 26px; }
  .contact-title { font-size: 11px; font-weight: 300; line-height: 16px; margin-bottom: 10px; }
  .contact-list { list-style: none; font-size: 12px; font-weight: 300; line-height: 19px; }
  .contact-list li { display: flex; align-items: flex-start; gap: 7px; }
  .contact-icon { width: 12px; height: 12px; flex: none; margin-top: 4px; }
  .contact-address { line-height: 18px; }
</style>
</head>
<body>
<main class="canvas">

  <section class="card card--front" aria-label="명함 앞면">
    <svg class="card-shape" viewBox="0 0 540 300" preserveAspectRatio="none" aria-hidden="true">
      <path d="M312 0 L350 0 C300 130 340 250 540 236 L540 270 C300 300 232 150 312 0 Z" fill="var(--green-deep)"/>
    </svg>
    <p class="front-website">www.arcvolley-example.co.kr</p>
    <div class="brand"><span class="brand-dot"></span><span class="brand-name">ARC VOLLEY</span></div>
  </section>

  <section class="card card--back" aria-label="명함 뒷면">
    <svg class="card-shape" viewBox="0 0 540 300" preserveAspectRatio="none" aria-hidden="true">
      <path d="M0 205 C60 212 110 255 200 255 C330 255 420 100 540 92 L540 116 C440 126 350 282 200 282 C100 282 55 232 0 228 Z" fill="var(--paper)"/>
    </svg>
    <div class="contact">
      <p class="contact-name">박 서 윤</p>
      <p class="contact-title">대표</p>
      <ul class="contact-list">
        <li>
          <svg class="contact-icon" viewBox="0 0 12 12" aria-hidden="true"><circle cx="6" cy="6" r="5.5" fill="#fff"/></svg>
          <span>arcvolley</span>
        </li>
        <li>
          <svg class="contact-icon" viewBox="0 0 12 12" aria-hidden="true"><path d="M2.5 1 L4.5 1 L5.2 3.6 L4 4.6 C4.7 6 5.9 7.3 7.4 8 L8.4 6.8 L11 7.5 L11 9.5 C11 10.3 10.3 11 9.5 11 C5 11 1 7 1 2.5 C1 1.7 1.7 1 2.5 1 Z" fill="#fff"/></svg>
          <span>010-8472-3916</span>
        </li>
        <li>
          <svg class="contact-icon" viewBox="0 0 12 12" aria-hidden="true"><rect x="0.5" y="2" width="11" height="8" rx="1" fill="#fff"/><path d="M1 2.6 L6 6.4 L11 2.6" stroke="var(--green)" stroke-width="1" fill="none"/></svg>
          <span>seoyun.park@arcvolley-example.co.kr</span>
        </li>
        <li>
          <svg class="contact-icon" viewBox="0 0 12 12" aria-hidden="true"><circle cx="6" cy="6" r="5" stroke="#fff" stroke-width="1.2" fill="none"/><ellipse cx="6" cy="6" rx="2.2" ry="5" stroke="#fff" stroke-width="1" fill="none"/><path d="M1 6 H11" stroke="#fff" stroke-width="1"/></svg>
          <span>www.arcvolley-example.co.kr</span>
        </li>
        <li>
          <svg class="contact-icon" viewBox="0 0 12 12" aria-hidden="true"><path d="M6 0.5 C3.6 0.5 2 2.2 2 4.4 C2 7.4 6 11.5 6 11.5 C6 11.5 10 7.4 10 4.4 C10 2.2 8.4 0.5 6 0.5 Z" fill="#fff"/><circle cx="6" cy="4.4" r="1.5" fill="var(--green)"/></svg>
          <span class="contact-address">경기도 용인시 수지구 풍덕천로 456<br>미래타워 5층 501호, 502호</span>
        </li>
      </ul>
    </div>
    <div class="brand"><span class="brand-dot"></span><span class="brand-name">ARC VOLLEY</span></div>
  </section>

</main>
</body>
</html>
```